Billboard Design for Modern Dispensary

Hello!
We need a eye-catching 12' x 24' billboard designed for a very successful, modern cannabis dispensary on the Oregon coast, United States. Because of rules, we cannot have any marijuana leafs or other cannabis related images (flower, joints, smoke, etc). We can use the words "Shop" or "Dispensary" - we cannot use the words "cannabis", "marijuana".

Some ideas we had are 3 words stacked on left or center of billboard - maybe across bottom we have horizontal logo and the following words - “South of bridge in Marlow Cove”
Another idea is to have a small bubble in bottom/top corner with image of our dog (face only) - with some words around it - like "BONUS Shop Dog" or "Cute Shop Dog" or "Best Shop Dog" or "Friendly Staff"

here's some 3 word examples:
ENJOY
YOUR
TRIP

or

FEEL
GOOD
JUST
AHEAD

or

GOOD
VIBES
ONLY

or

GOOD
TIMES
CHILL
VIBES

I have attached our logo. I have also included a stacked logo version (vertical, not horizontal). the formats are .EPS and .PDF - the logos were created in Affinity Design 2.x.

Our website is lunarwharf.com if you want to see more images, etc about our dispensary.

Artwork Requirements:
The billboard is 12' tall x 25' wide
The artwork needs to be 1”=1’ @ 300dpi
Please add 6” of bleed all around so your total artwork is 13”x26”
Final deliverable should be .Ai file.

Font styles to use
Sans Serif

Colors
0054AA
0677BA
7BADD7
CADEEF
E8F1F8

Requirements
Nice to have
• See the project description - we included some ideas to consider.
Should not have
• No cannabis images, like flower, cannabis leaves, paraphenlia, cartridges, joints, etc.

```html
<!DOCTYPE html>
<html lang="en">
<head>
<meta charset="utf-8">
<title>Lunar Wharf – Billboard</title>
<link rel="stylesheet" href="https://fonts.googleapis.com/css2?family=Poppins:wght@400;700;800&family=Oswald:wght@400&display=swap">
<style>
  :root {
    --page-bg: #dedcdd;
    --navy: #0d1f4f;
    --sky-deep: #2f86d0;
    --sky-mid: #4a9ad8;
    --sky-light: #7badd7;
    --brand-blue: #0677ba;
    --stripe-blue: #0b63e0;
    --tagline-blue: #3a8fd0;
    --swoosh-gray: #b9b9bb;
    --white: #ffffff;
  }
  * { margin: 0; padding: 0; box-sizing: border-box; }
  html, body { width: 1200px; height: 1200px; overflow: hidden; }
  body { background: var(--page-bg); position: relative; font-family: "Poppins", sans-serif; }

  .billboard {
    position: absolute;
    left: 50px; top: 328px;
    width: 1100px; height: 543px;
    overflow: hidden;
    box-shadow: 0 14px 24px rgba(0,0,0,0.22);
  }
  .billboard-art { position: absolute; inset: 0; width: 100%; height: 100%; }

  .headline {
    position: absolute;
    left: 52px; top: 88px;
    color: var(--navy);
    font-weight: 800;
    font-size: 86px;
    line-height: 101px;
    letter-spacing: -0.5px;
  }
  .headline span { display: block; }

  .bonus {
    position: absolute;
    left: 700px; top: 48px;
    width: 280px;
    text-align: center;
    color: var(--navy);
    font-weight: 700;
    font-size: 45px;
    line-height: 50px;
  }
  .bonus .bonus-label { display: block; text-transform: uppercase; }

  .tagline {
    position: absolute;
    left: 52px; top: 453px;
    font-family: "Oswald", sans-serif;
    font-weight: 400;
    font-size: 52px;
    line-height: 70px;
    color: var(--tagline-blue);
    letter-spacing: 0.2px;
  }

  .brand {
    position: absolute;
    left: 718px; top: 443px;
    display: flex; align-items: center; gap: 16px;
  }
  .brand-dot {
    width: 76px; height: 76px; border-radius: 50%;
    background: var(--brand-blue);
  }
  .brand-name {
    font-family: "Poppins", sans-serif;
    font-weight: 400;
    font-size: 38px;
    color: var(--brand-blue);
    text-transform: uppercase;
  }
</style>
</head>
<body>
  <section class="billboard">
    <svg class="billboard-art" viewBox="0 0 1100 543" xmlns="http://www.w3.org/2000/svg">
      <defs>
        <linearGradient id="skyGradient" x1="0" y1="0" x2="1" y2="0.3">
          <stop offset="0" stop-color="#3f8fd2"/>
          <stop offset="0.55" stop-color="#4d9dd9"/>
          <stop offset="1" stop-color="#6fb3e2"/>
        </linearGradient>
        <linearGradient id="coastGradient" x1="0" y1="0" x2="0" y2="1">
          <stop offset="0" stop-color="#8cc3ea"/>
          <stop offset="0.35" stop-color="#6f9a6a"/>
          <stop offset="0.6" stop-color="#2f7f96"/>
          <stop offset="1" stop-color="#1f6f8a"/>
        </linearGradient>
        <linearGradient id="coastFade" x1="0" y1="0" x2="1" y2="0">
          <stop offset="0" stop-color="#fff" stop-opacity="0"/>
          <stop offset="0.35" stop-color="#fff" stop-opacity="1"/>
        </linearGradient>
        <mask id="coastMask">
          <rect x="560" y="0" width="540" height="543" fill="url(#coastFade)"/>
        </mask>
        <radialGradient id="dogGradient" cx="0.5" cy="0.45" r="0.6">
          <stop offset="0" stop-color="#d9b78a"/>
          <stop offset="0.7" stop-color="#a78762"/>
          <stop offset="1" stop-color="#5a4433"/>
        </radialGradient>
      </defs>

      <rect class="sky" width="1100" height="543" fill="url(#skyGradient)"/>

      <g role="img" aria-label="Photo of a rocky Oregon coast cove with forest and surf">
        <rect x="560" y="0" width="540" height="460" fill="url(#coastGradient)" mask="url(#coastMask)"/>
      </g>

      <path class="accent-stripe" d="M0,396 C220,404 460,420 660,440 L0,446 Z" fill="var(--stripe-blue)"/>
      <path class="swoosh" d="M690,440 C840,392 970,356 1100,326 V420 C1000,400 860,404 760,432 Z" fill="var(--swoosh-gray)"/>
      <path class="footer-band" d="M0,442 C300,441 560,440 740,428 C880,410 1000,402 1100,412 V543 H0 Z" fill="var(--white)"/>

      <g class="thought-bubble">
        <circle cx="557" cy="177" r="131" fill="var(--white)"/>
        <circle cx="557" cy="177" r="118" fill="url(#dogGradient)" role="img" aria-label="Photo of the shop dog"/>
        <circle cx="663" cy="303" r="26" fill="var(--white)"/>
        <circle cx="663" cy="303" r="18" fill="var(--tagline-blue)"/>
      </g>
    </svg>

    <h1 class="headline">
      <span>SLEEP</span>
      <span>BETTER</span>
      <span>TONIGHT</span>
    </h1>

    <p class="bonus"><span class="bonus-label">Bonus</span>Shop Dog</p>

    <p class="tagline">South of bridge in Marlow Cove</p>

    <div class="brand">
      <span class="brand-dot"></span>
      <span class="brand-name">Lunar Wharf</span>
    </div>
  </section>
</body>
</html>
```